Advert for Newspaper
National Newspaper ad for vantor wellness week
Advert for Newspaper - Medical
Creative Brief
Medical
Medical Optometrists, offering services to all ages but in particular those over 40 years of age who are more likely to suffer from glaucoma
The advert has to be 201mm in width and 90mm high. This is a direct response advert so the key things are the benefits, and the cut price and Call now! Please design using Indesign or illustrator with the original files also sent as well as a pdf. It can be full colour. The text in the advert has to include: Do you want the ultimate glaucoma detection and monitoring? The first private glaucoma clinic with 24 hour pressure monitoring in the UK* 24 hour pressure monitoring Advanced KRTL nerve fibre layer scans Gold standard visual fields Award winning care Fairlow Optometrists - Winners of independent practice of the year Vantor Wellness Week Limited time special offer for the month of September** Normal Price £2500 Special limited time offer £600 Book your appointment Call Now on 01632 960418 www.pelmarcare.co.uk (for more information) Small print - *Using corneal dimensional change **For eligible glaucoma sufferers only ask for T’s & C’s

```html
<!DOCTYPE html>
<html lang="en">
<head>
<meta charset="utf-8">
<title>Fairlow Optometrists – Glaucoma Clinic Advert</title>
<link href="https://fonts.googleapis.com/css2?family=Oswald:wght@500;700&family=Open+Sans:wght@400;600;700;800&display=swap" rel="stylesheet">
<style>
  :root {
    --page-bg: #ececec;
    --paper: #ffffff;
    --orange: #f07a1c;
    --teal: #2a9aa5;
    --teal-dark: #1f7f89;
    --navy: #1d2b4a;
    --grey: #8c8f94;
    --grey-light: #e3e4e6;
    --photo-warm: #c9b7a3;
    --photo-cool: #9fb7c4;
  }
  * { box-sizing: border-box; margin: 0; padding: 0; }
  html, body { width: 1200px; height: 845px; overflow: hidden; background: var(--page-bg); }
  body { font-family: "Open Sans", Arial, sans-serif; color: var(--navy); }

  .advert {
    position: absolute; left: 20px; top: 162px;
    width: 1160px; height: 520px;
    background: var(--paper); overflow: hidden;
    box-shadow: 0 2px 10px rgba(0,0,0,.12);
  }
  .couple-photo {
    position: absolute; left: 0; top: 0; width: 640px; height: 464px;
    background:
      linear-gradient(90deg, rgba(255,255,255,0) 50%, var(--paper) 100%),
      linear-gradient(160deg, var(--photo-cool) 0%, var(--photo-warm) 55%, #b49a84 100%);
  }
  .headline {
    position: absolute; left: 340px; right: 20px; top: 14px;
    font-family: "Oswald", "Arial Narrow", sans-serif; font-weight: 700;
    font-size: 43px; line-height: 1.05; color: var(--orange);
    text-align: center; text-transform: uppercase; letter-spacing: .3px;
    white-space: nowrap;
  }
  .subhead {
    position: absolute; right: 20px; top: 112px;
    font-weight: 800; font-size: 21px; line-height: 1.25;
    color: var(--teal); text-align: right; white-space: nowrap;
  }
  .benefits {
    position: absolute; right: 20px; top: 246px; list-style: none;
    font-weight: 800; font-size: 19px; line-height: 1.4;
    color: var(--navy); text-align: right; text-transform: uppercase;
    white-space: nowrap;
  }
  .benefits li::after { content: " \2022"; color: var(--orange); }

  .normal-price {
    position: absolute; left: 392px; top: 302px; width: 116px; height: 80px;
    background: rgba(255,255,255,.85); border-radius: 6px;
    text-align: center; color: var(--navy); padding-top: 8px;
  }
  .normal-price .label { font-size: 11px; font-weight: 700; text-transform: uppercase; }
  .normal-price .amount {
    display: inline-block; font-family: "Oswald", sans-serif; font-size: 34px; font-weight: 700;
    line-height: 1.2;
  }
  .offer-badge {
    position: absolute; left: 500px; top: 226px; width: 152px; height: 152px;
    border-radius: 50%; background: var(--orange); border: 5px solid var(--paper);
    color: var(--paper); text-align: center; padding-top: 26px;
    box-shadow: 0 2px 6px rgba(0,0,0,.25);
  }
  .offer-badge .label { font-size: 12px; font-weight: 800; line-height: 1.15; text-transform: uppercase; }
  .offer-badge .amount { font-family: "Oswald", sans-serif; font-size: 50px; font-weight: 700; line-height: 1.05; }

  .campaign {
    position: absolute; right: 20px; top: 384px;
    text-align: right; font-weight: 800; font-size: 13px; line-height: 1.3;
    text-transform: uppercase; white-space: nowrap;
  }
  .campaign .week { color: var(--teal-dark); }
  .campaign .offer { color: var(--teal-dark); }
  .campaign .month { color: var(--orange); }

  .small-print {
    position: absolute; right: 20px; top: 449px;
    font-size: 8px; line-height: 1; color: var(--grey); white-space: nowrap;
  }

  .contact-band {
    position: absolute; left: 0; bottom: 0; width: 100%; height: 56px;
    background: var(--teal); color: var(--paper);
  }
  .practice {
    position: absolute; left: 0; top: 0; height: 56px; width: 250px;
    background: var(--paper); display: flex; align-items: center; gap: 12px; padding-left: 16px;
  }
  .practice .mark { width: 28px; height: 28px; border-radius: 50%; background: var(--teal); flex: none; }
  .practice .name { font-weight: 700; font-size: 17px; color: var(--teal-dark); line-height: 1.05; }
  .practice .award { width: 30px; height: 30px; border-radius: 50%; background: var(--grey-light); margin-left: auto; margin-right: 14px; }

  .booking { position: absolute; left: 270px; top: 5px; }
  .booking .label { font-size: 10px; font-weight: 700; text-transform: uppercase; letter-spacing: .3px; }
  .booking .phone { display: flex; align-items: center; gap: 8px; font-family: "Oswald", sans-serif; font-size: 28px; font-weight: 700; line-height: 1.1; }
  .website { position: absolute; right: 20px; top: 15px; font-weight: 800; font-size: 20px; }
</style>
</head>
<body>
  <main class="advert">
    <div class="couple-photo" role="img" aria-label="Smiling older couple relaxing together at home"></div>

    <h1 class="headline">Do you want the ultimate glaucoma<br>detection and monitoring?</h1>
    <p class="subhead">The First Private Glaucoma Clinic With 24 Hour<br>Pressure Monitoring In The UK*</p>

    <ul class="benefits">
      <li>24 Hour Pressure Monitoring</li>
      <li>Advanced KRTL Nerve Fibre Layer Scans</li>
      <li>Gold Standard Visual Fields</li>
      <li>Award Winning Care</li>
    </ul>

    <div class="normal-price">
      <div class="label">Normal Price</div>
      <div class="amount">£2500</div>
    </div>
    <div class="offer-badge">
      <div class="label">Special<br>Limited Time<br>Offer</div>
      <div class="amount">£600</div>
    </div>

    <div class="campaign">
      <div class="week">Vantor Wellness Week</div>
      <div class="offer">Limited time special offer</div>
      <div class="month">For the month of September**</div>
    </div>

    <p class="small-print">*Using corneal dimensional change &nbsp;|&nbsp; **For eligible glaucoma sufferers only ask for T’s &amp; C’s</p>

    <footer class="contact-band">
      <div class="practice">
        <span class="mark"></span>
        <span class="name">Fairlow<br>Optometrists</span>
        <span class="award"></span>
      </div>
      <div class="booking">
        <div class="label">Book your appointment, call now on</div>
        <div class="phone">
          <svg width="22" height="22" viewBox="0 0 24 24" aria-hidden="true"><path fill="#fff" d="M6.6 10.8a15.1 15.1 0 0 0 6.6 6.6l2.2-2.2c.3-.3.7-.4 1-.2 1.1.4 2.3.6 3.6.6.6 0 1 .4 1 1V20c0 .6-.4 1-1 1A17 17 0 0 1 3 4c0-.6.4-1 1-1h3.5c.6 0 1 .4 1 1 0 1.3.2 2.5.6 3.6.1.3 0 .7-.2 1z"/></svg>
          01632 960418
        </div>
      </div>
      <div class="website">www.pelmarcare.co.uk</div>
    </footer>
  </main>
</body>
</html>
```